Elegant brochure for BtoB Wine event in Asia

I need a design for a 4 pages brochure promoting 2 wine in Asia (China and Taiwan), A4 format. These 2 events will be open to professionals only. The hotel is located in the heart of Asia. The design has to show as well as the topic of these 2 wine, which is the wine. Colors can be black and red. The hotel is located in the heart of the city, in the heart of the city. ...
Target Market(s)
Wine industry. European wineries and Asian wine importers-distributors.
Industry/Entity Type
Events
Requirements
Must have
- Show the 2 main ideas: Wine and Asia High level, exclusivity, luxury atmosphere
Nice to have
- It would be great if page 3 and page 5 could be writable.

```html
<!DOCTYPE html>
<html lang="fr">
<head>
<meta charset="utf-8">
<title>European Wines Discovery Tour 2017 – Brochure</title>
<link href="https://fonts.googleapis.com/css2?family=Roboto+Condensed:ital,wght@0,300;0,400;0,700;1,400&display=swap" rel="stylesheet">
<style>
:root{
  --wine:#b8121c;
  --wine-bright:#d2232a;
  --wine-dark:#7d0a12;
  --wine-deep:#560710;
  --ink:#1c1c1c;
  --charcoal:#333132;
  --grey:#c9c9c9;
  --paper:#ffffff;
  --backdrop:#2b2421;
}
*{box-sizing:border-box;margin:0;padding:0}
html,body{width:1200px;height:1200px;overflow:hidden;background:var(--backdrop);font-family:"Roboto Condensed",Arial,sans-serif;color:var(--ink)}
.spread{position:absolute;left:160px;width:880px;height:568px;display:flex;box-shadow:0 6px 18px rgba(0,0,0,.45)}
.spread--outer{top:18px}
.spread--inner{top:614px}
.page{position:relative;width:440px;height:568px;overflow:hidden}

/* ---------- back page : tasting form ---------- */
.page--form{background:radial-gradient(ellipse at 50% 40%,var(--wine-bright) 0%,var(--wine) 55%,var(--wine-dark) 100%);color:var(--paper)}
.form-title{position:absolute;top:26px;left:24px;font-size:16.6px;font-weight:400;letter-spacing:.2px}
.card{position:absolute;left:27px;width:381px;background:var(--paper);border-radius:8px;color:var(--ink);font-size:6.6px;padding:0 12px}
.card--profile{top:60px;height:224px;padding-top:18px}
.card--importer{top:330px;height:160px;padding-top:8px}
.field{display:flex;align-items:flex-end;gap:3px;height:14px}
.field .line{flex:1;border-bottom:.7px solid #555;height:7px}
.field--pair .line{margin-right:4px}
.gap{height:6px}
.blank-line{border-bottom:.7px solid #555;height:14px}
.surface{display:flex;align-items:flex-end;gap:2px;height:14px;margin-top:12px}
.surface .short{width:38px;border-bottom:.7px solid #555;height:7px}
.surface .mid{width:54px;border-bottom:.7px solid #555;height:7px}
.ask{position:absolute;left:40px;font-size:6.6px;display:flex;align-items:center;width:330px}
.ask span.q{flex:1}
.tick{display:inline-block;width:8px;height:8px;background:var(--paper);margin:0 3px 0 6px;vertical-align:middle}
.ask--1{top:296px}.ask--2{top:311px}
.logo-request{text-align:center;font-size:9.2px;margin:18px 0 6px}
.sign-row{display:flex;justify-content:space-between;width:230px;margin-top:14px}
.contact{position:absolute;top:498px;left:0;width:440px;text-align:center;font-size:6.6px;line-height:14px}
.contact strong{font-size:8.6px}

/* ---------- cover ---------- */
.page--cover{background:radial-gradient(ellipse at 50% 45%,var(--wine-bright) 0%,var(--wine) 50%,var(--wine-dark) 100%);color:var(--paper)}
.cover-title{position:absolute;top:14px;width:100%;text-align:center;font-size:30px;font-weight:700;letter-spacing:-.3px}
.cover-sub{position:absolute;top:50px;width:100%;text-align:center;font-size:25px;font-weight:300;padding-left:4px}
.photo{position:absolute;width:84px;height:66px;background:linear-gradient(160deg,#5b3a33 0%,#2e1c1a 60%,#4a2e28 100%)}
.arch{position:absolute;left:108px;top:104px;width:222px;height:384px}
.arch-frame{position:absolute;inset:0}
.glass-art{position:absolute;left:9px;top:9px;width:204px;height:368px;border-radius:102px 102px 0 0;
  background:
    radial-gradient(ellipse 60% 34% at 50% 30%,#ffffff 0%,#ffffff 60%,rgba(255,255,255,0) 100%),
    radial-gradient(ellipse 40% 18% at 50% 62%,#ffffff 0%,#ffffff 55%,rgba(255,255,255,0) 100%),
    linear-gradient(180deg,var(--wine-dark) 0%,#f3dcde 14%,#ffffff 30%,#ffffff 60%,var(--wine-bright) 72%,var(--wine) 100%)}
.cities{position:absolute;left:24px;top:204px;width:180px;color:var(--ink);font-weight:700;font-size:24px;line-height:24px}
.cities .amp{color:var(--wine);font-weight:300;font-size:32px}
.cities .c2{display:block;padding-left:30px}
.date{position:absolute;left:14px;top:262px;width:84px;text-align:center}
.date .num{font-size:70px;font-weight:700;line-height:64px;letter-spacing:-3px}
.date .num small{font-size:26px;font-weight:400}
.date .month{font-size:14px;font-weight:700;margin-top:6px}
.pros{position:absolute;left:114px;top:284px;width:108px;font-weight:700;line-height:1}
.pros .big{font-size:25px}
.pros .mid{font-size:14.5px;margin:3px 0 8px}
.brand-mark{position:absolute;top:502px;width:100%;text-align:center;font-size:26px;color:var(--wine-dark);font-weight:400;letter-spacing:.5px}
.organiser{position:absolute;top:539px;width:100%;text-align:center;font-size:14.5px;font-weight:400}

/* ---------- inside left ---------- */
.page--about{background:var(--paper);font-size:6.8px;line-height:1.4}
.about-title{position:absolute;top:13px;width:100%;text-align:center;color:var(--wine);font-size:15px;font-weight:700}
.about-body{position:absolute;top:44px;left:19px;width:402px}
.about-body h3{font-size:9.6px;font-weight:700;margin-bottom:6px}
.about-body p{margin-bottom:6px}
.pitch{position:absolute;top:184px;left:19px;color:var(--wine);font-size:11px;font-weight:700}
.venue{position:absolute;top:203px;height:52px;color:var(--paper);font-size:7px;font-weight:700;line-height:1.35;padding:6px 20px}
.venue--taipei{left:0;width:210px;background:var(--wine)}
.venue--shenzhen{left:210px;width:230px;background:var(--charcoal);padding-left:14px}
.venue span{font-weight:400;display:block;text-transform:uppercase}
.why{position:absolute;top:262px;width:200px;text-align:justify;font-size:6.8px;line-height:1.38}
.why--taipei{left:19px}.why--shenzhen{left:225px}
.why h4{color:var(--wine);font-size:11.5px;font-weight:700;margin-bottom:5px}
.why p{margin-bottom:4px}

/* ---------- inside right ---------- */
.page--register{background:var(--paper);font-size:6.6px}
.formula-box{position:absolute;left:22px;top:0;width:118px;height:84px;background:var(--wine);color:var(--paper);padding:10px 9px}
.formula-box h3{font-size:12.5px;font-weight:400;line-height:1.3}
.formula-box p{font-size:6.8px;font-weight:700;margin-top:6px;line-height:1.5}
.includes{position:absolute;left:150px;top:10px;width:284px;font-size:6.2px;line-height:1.5}
.includes li{list-style:none}
.includes li.item::before{content:"";display:inline-block;width:4px;height:4px;border-radius:50%;background:var(--wine);margin-right:3px;vertical-align:middle}
.includes li.head{font-weight:700}
.reg-title{position:absolute;top:96px;left:22px;color:var(--wine);font-size:13.5px;font-weight:700}
.reg-note{position:absolute;top:98px;left:261px;font-size:6.3px;line-height:1.4}
.reg-fields{position:absolute;top:118px;left:24px;width:396px}
.reg-row{display:flex;align-items:flex-end;height:15px}
.reg-row .lab{width:56px}
.reg-row .line{flex:1;border-bottom:.6px solid #777;height:8px}
.reg-row .mid{width:130px;flex:none;margin-right:6px}
.travellers{margin-top:6px}
.plan-title{position:absolute;top:228px;left:30px;color:var(--wine);font-size:11.5px}
.plan{position:absolute;top:245px;left:30px;width:330px}
.plan-row{display:flex;align-items:center;height:15px}
.box{width:8px;height:8px;border:.6px solid #777;margin-right:5px;flex:none;display:inline-block;vertical-align:middle}
.plan-row .opt{flex:1}
.plan-row .price{color:var(--wine);font-weight:700;font-size:9.6px;width:46px}
.options{position:absolute;top:294px;left:24px;width:396px;border:.8px solid #888;border-top:none}
.options-head{display:flex;align-items:center;height:18px;background:var(--grey);padding-left:8px}
.options-head .t{color:var(--wine);font-size:11.5px;width:134px}
.options-head .h{font-size:6.3px;width:112px}
.opt-row{display:flex;border-top:.8px solid #888}
.opt-row .lab{width:124px;padding:5px 6px;line-height:1.55;border-right:.8px solid #888}
.opt-row .col{width:112px;padding:5px 0 0 14px;line-height:1.55;border-right:.8px solid #888}
.opt-row .col:last-child{border-right:none}
.yn .box{width:7px;height:7px;margin-right:3px}
.yn span{margin-right:8px}
.opt-total{height:19px;background:var(--grey);text-align:right;padding:6px 52px 0 0;font-weight:700;font-size:6.3px;border-top:.8px solid #888}
.total-text{position:absolute;top:462px;left:24px;width:396px;font-size:6.2px;line-height:1.4}
.bank{position:absolute;top:494px;left:24px;width:396px;height:52px;background:var(--wine);color:var(--paper);display:flex;align-items:center;padding:0 8px;font-size:6.2px;line-height:1.4}
.bank dl{display:grid;grid-template-columns:46px 160px}
.bank .note{font-style:italic;border-left:1px solid var(--paper);border-radius:4px 0 0 4px;padding-left:8px;width:172px}
.footnote{position:absolute;top:552px;width:100%;text-align:center;font-style:italic;font-size:5.6px}
</style>
</head>
<body>

<section class="spread spread--outer">
  <div class="page page--form">
    <h2 class="form-title">PRESENTATION POUR LE CARNET DE DEGUSTATION</h2>

    <div class="card card--profile">
      <div class="field">Région viticole :<span class="line"></span></div>
      <div class="field">Société sous laquelle vous souhaitez apparaitre dans le catalogue :<span class="line"></span></div>
      <div class="gap"></div>
      <div class="field field--pair">Nom :<span class="line"></span>Prénom :<span class="line"></span></div>
      <div class="field">Fonction :<span class="line"></span></div>
      <div class="field field--pair">E-mail :<span class="line"></span>Site Internet :<span class="line"></span></div>
      <div class="field field--pair">Tel :<span class="line"></span>Fax :<span class="line"></span></div>
      <div class="gap"></div>
      <div class="field">Description de la société (vos points forts en 4 lignes) :</div>
      <div class="blank-line"></div>
      <div class="blank-line"></div>
      <div class="blank-line"></div>
      <div class="blank-line"></div>
      <div class="surface">La surface du vignoble :<span class="short"></span>hectares – Production :<span class="mid"></span>hl ou<span class="short"></span>bouteilles (0,75 l).</div>
    </div>

    <div class="ask ask--1"><span class="q">Importateur :Avez-vous un ou plusieurs importateur(s) sur ce pays :</span><span class="tick"></span>OUI<span class="tick"></span>NON</div>
    <div class="ask ask--2"><span class="q">Souhaitez-vous qu'on le mentionne sur le carnet de dégustation :</span><span class="tick"></span>OUI<span class="tick"></span>NON</div>

    <div class="card card--importer">
      <div class="field">Merci de nous donner le(s) nom(s) et coordonnées</div>
      <div class="blank-line"></div>
      <div class="blank-line"></div>
      <p class="logo-request">Merci d'envoyer votre logo avec la présentation</p>
      <div class="field">Fait à :</div>
      <div class="field">Le :</div>
      <div class="field">Par :</div>
      <div class="sign-row"><span>Cachet de l'entreprise :</span><span>Signature :</span></div>
    </div>

    <div class="contact">
      <strong>Pour nous contacter :</strong><br>
      Vinelle Events Shenzhen<br>
      Lin Meihua : +86 (0) 755 0000 1234 - lmeihua@vinelle-events.net<br>
      Unit 5, 2nd floor, Harbour View Building, Coast Road 12, Nanshan district, Shenzhen, China
    </div>
  </div>

  <div class="page page--cover">
    <h1 class="cover-title">European Wines Discovery</h1>
    <p class="cover-sub">Tour 2017</p>

    <div class="photo" style="left:14px;top:169px" role="img" aria-label="Photo: crowd of professionals tasting wine"></div>
    <div class="photo" style="left:14px;top:246px" role="img" aria-label="Photo: visitors around tasting tables"></div>
    <div class="photo" style="left:14px;top:323px" role="img" aria-label="Photo: busy wine fair room"></div>
    <div class="photo" style="left:14px;top:400px" role="img" aria-label="Photo: guests with glasses at a stand"></div>
    <div class="photo" style="left:342px;top:174px" role="img" aria-label="Photo: producer pouring wine"></div>
    <div class="photo" style="left:342px;top:251px" role="img" aria-label="Photo: bottles lined up on a table"></div>
    <div class="photo" style="left:342px;top:329px" role="img" aria-label="Photo: tasting table with bottles"></div>
    <div class="photo" style="left:342px;top:405px" role="img" aria-label="Photo: visitors at a wine stand"></div>

    <div class="arch">
      <div class="glass-art" role="img" aria-label="Illustration: large white wine glass shaped as a map of Asia, with a red wine drop and the script title in Asia"></div>
      <svg class="arch-frame" width="222" height="384" viewBox="0 0 222 384" aria-hidden="true">
        <path d="M6 380 V111 A105 105 0 0 1 216 111 V380 Z" fill="none" stroke="var(--wine-dark)" stroke-width="6"/>
      </svg>
      <div class="cities">Taipei<span class="amp">&amp;</span><span class="c2">Shenzhen</span></div>
      <div class="date">
        <div class="num">5<small>&amp;</small>7</div>
        <div class="month">DECEMBRE</div>
      </div>
      <div class="pros">
        <div class="big">400 WINE</div>
        <div class="mid">PROFESSIONALS</div>
        <div class="big">IN 2 DAYS</div>
      </div>
    </div>

    <p class="brand-mark">VINELLE EVENTS</p>
    <p class="organiser">UN EVENEMENT ORGANISE PAR VINELLE EVENTS</p>
  </div>
</section>

<section class="spread spread--inner">
  <div class="page page--about">
    <h2 class="about-title">EUROPEAN WINES DISCOVERY TOUR 2017 IN ASIA</h2>
    <div class="about-body">
      <h3>L'ORGANISATEUR</h3>
      <p><strong>Vous nous connaissez ou avez déjà bénéficié de nos services, sans le savoir.</strong><br>
      Une agence événementielle, avec une équipe expérimentée, bénéficiant d'une longue expérience dans l'organisation d'événements professionnels sur le marché asiatique. Travaillant très souvent dans l'ombre des principaux organisateurs, vous propose aujourd'hui 2 événements professionnels pour une efficacité maximale.<br>
      Nous souhaitons proposer aux producteurs de vins européens, une alternative aux offres existantes, en leur apportant de la nouveauté à travers des bases de données mises à jour quotidiennement, sur des marchés, où tout le monde le sait l'évolution est permanente.</p>
      <p>A travers, notre activité, nous connaissons l'ensemble de la filière, allant de l'importateur, du distributeur jusqu'aux prescripteurs finaux, que sont les sommeliers, les F&amp;B entres autres.<br>
      Pour en savoir plus sur nous : www.vinelle-events.net<br>
      <strong>Notre proposition – notre engagement</strong></p>
    </div>
    <p class="pitch">2 jours, 2 villes, 2 pays, combien de jours de prospection économisé pour vous ?</p>

    <div class="venue venue--taipei"><span>Taipei, Taiwan – Grand Regency</span>On December 5th, 1pm-7pm<br>50 producteurs de vins européens<br>200 visiteurs professionnels</div>
    <div class="venue venue--shenzhen"><span>Shenzhen, China - Crestview</span>On December 7th, 1pm-7pm<br>50 producteurs de vins européens<br>200 visiteurs professionnels</div>

    <div class="why why--taipei">
      <h4>POURQUOI TAIPEI - TAIWAN ?</h4>
      <p><strong>Le marché :</strong> Avec une population de plus de 23 millions, Taiwan est un marché important pour l'importation de boissons alcoolisées. Au cours des six dernières années, une augmentation annuelle de la consommation a été enregistrée, soit 8,6% pour le vin et 8,8 % pour les spiritueux. Taiwan figure au nombre des 5 plus importants marchés pour le vin en Asie.</p>
      <p><strong>Les opportunités :</strong> Émergence de nouveaux groupes de consommateurs parmi les citadins et les femmes. Forte demande pour le vin en raison de l'augmentation du nombre de touristes en provenance de la Chine continentale. Des habitudes de consommation en pleine évolution avec l'arrivée de nouveaux consommateurs ayant déjà développé une préférence pour le vin.</p>
      <p>Comme Taiwan, n'est pas considéré comme un marché de volume, souvent à tort, il n'y aucune exposition vin majeure pour les professionnels, beaucoup de dégustations pour le grand public. Ce qui a pour conséquence de mobiliser les professionnels lorsqu'un événement est organisé, et d'être plutôt bien accueilli.</p>
      <p><strong>Le + :</strong> Taiwan étant à proximité de sa grande sœur chinoise, et face à Xiamen, ville chinoise côtière particulièrement riche et dynamique, depuis que les relations en la Grande Chine et Taiwan se sont normalisées, de nombreux importateurs taiwanais ont ouvert un bureau à Xiamen, pour leur développement sur la Chine continentale.</p>
      <p><strong>Vinelle Events a déjà organisé un événement majeur à Taipei, qui a comptabilisé plus de 500 visiteurs professionnels</strong></p>
    </div>

    <div class="why why--shenzhen">
      <h4>POURQUOI SHENZHEN ?</h4>
      <p><strong>Le marché :</strong> Situé en bordure de Hong Kong, en 1979 une partie de son territoire acquiert le statut de zone économique spéciale et devient l'un des principaux lieux d'expérimentation de la politique d'ouverture aux investissements étrangers. Bénéficiant de sa position géographique privilégiée, elle connaît un essor économique et démographique spectaculaire. Aujourd'hui, elle compte environ 11 millions d'habitants et constitue une des municipalités les plus riches de Chine. Elle fait partie de la mégalopole chinoise du delta de la Rivière des Perles. La croissance économique de Shenzhen est de 26 % par an en moyenne depuis 1980.</p>
      <p><strong>Les opportunités :</strong> La population de Shenzhen est jeune, aisée, et bénéficie de l'influence de sa voisine hongkongaise sur les modes de consommation. Le vin devient une boisson à la mode. C'est à Shenzhen que sont localisés tous les sièges sociaux des principales sociétés chinoises d'IT et de grands groupes technologiques étrangers, attirant tous les jeunes talents de la nouvelle économie, fraîchement sortis des meilleures universités.</p>
      <p><strong>Le + :</strong> Shenzhen a vu s'implanter un nombre très important d'importateurs hongkongais, désireux de se développer sur la Chine continentale, ce qui en fait aussi une porte d'entrée pour Hong Kong.</p>
      <p><strong>Vinelle Events a un bureau à Shenzhen, et a déjà organisé 2 événements majeurs qui ont attiré plus de 350 visiteurs professionnels.</strong></p>
    </div>
  </div>

  <div class="page page--register">
    <div class="formula-box">
      <h3>LA FORMULE DE PARTICIPATION</h3>
      <p>1 ville &nbsp;: 1 500 Eur<br>2 villes : 2 500 Eur</p>
    </div>
    <ul class="includes">
      <li class="head">Les prix de participation comprennent :</li>
      <li class="item">Présentation catalogue (présentation en page 4), une page + logo,</li>
      <li class="item">Une table avec nappe blanche, chevalet société, badge,</li>
      <li class="item">2 Seaux à glaces, un crachoir, une corbeille de pain ou crackers, petites bouteilles d'eau,</li>
      <li class="item">L'envoi de 24 bouteilles en échantillons.</li>
      <li class="head">N'est pas compris :</li>
      <li class="item">Votre déplacement depuis la France et les vols intérieurs,</li>
      <li class="item">Votre hébergement.</li>
    </ul>

    <h2 class="reg-title">FICHE D'INSCRIPTION EXPOS ASIE 2017</h2>
    <p class="reg-note">A retourner par e-mail à contact@vinelle-events.com<br>Avant le 1<sup>er</sup> novembre 2017</p>

    <div class="reg-fields">
      <div class="reg-row"><span class="lab">Entreprise &nbsp;&nbsp;&nbsp;:</span><span class="line"></span></div>
      <div class="reg-row"><span class="lab">Nom du Contact :</span><span class="line"></span></div>
      <div class="reg-row"><span class="lab">Adresse &nbsp;&nbsp;&nbsp;&nbsp;&nbsp;&nbsp;:</span><span class="line"></span></div>
      <div class="reg-row"><span class="lab">Tél. &nbsp;&nbsp;&nbsp;&nbsp;&nbsp;&nbsp;&nbsp;&nbsp;&nbsp;&nbsp;:</span><span class="line mid"></span>E-mail :<span class="line"></span></div>
      <div class="reg-row travellers">Nom et Prénom de la ou des personne(s) faisant le déplacement :</div>
      <div class="reg-row"><span class="line mid" style="width:184px"></span>Portable :<span class="line"></span></div>
    </div>

    <h3 class="plan-title">FORMULE</h3>
    <div class="plan">
      <div class="plan-row"><span class="box"></span><span class="opt">TAIPEI, le 5 décembre 2017</span><span class="price">1,500 Eur</span></div>
      <div class="plan-row"><span class="box"></span><span class="opt">TAIPEI, le 5 décembre 2017&amp; SHENZHEN, le 7 décembre 2017</span><span class="price">2,500 Eur</span></div>
      <div class="plan-row"><span class="box"></span><span class="opt">SHENZHEN, le 7 décembre 2017</span><span class="price">1,500 Eur</span></div>
    </div>

    <div class="options">
      <div class="options-head"><span class="t">OPTIONS</span><span class="h">04/12 - Taipei, Grand Regency</span><span class="h">06/12 - Shenzhen, Crestview</span></div>
      <div class="opt-row">
        <div class="lab"><strong>Hébergement</strong><br>Une personne = 150 Eur/nuit<br>Deux personnes = 165 Eur/nuit<br>( <span class="box" style="width:7px;height:7px"></span> double <span class="box" style="width:7px;height:7px"></span> twin)<br>Extra-room</div>
        <div class="col yn"><br><span class="box"></span><span>OUI</span><span class="box"></span>NON<br><span class="box"></span><span>OUI</span><span class="box"></span>NON<br><span class="box"></span><span>OUI</span><span class="box"></span>NON</div>
        <div class="col yn"><br><span class="box"></span><span>OUI</span><span class="box"></span>NON<br><span class="box"></span><span>OUI</span><span class="box"></span>NON<br><span class="box"></span><span>OUI</span><span class="box"></span>NON</div>
        <div class="col" style="width:48px"></div>
      </div>
      <div class="opt-row">
        <div class="lab"><strong>Interprète</strong> (150 Eur/ville)</div>
        <div class="col yn" style="padding-top:6px"><span class="box"></span><span>OUI</span><span class="box"></span>NON</div>
        <div class="col yn" style="padding-top:6px"><span class="box"></span><span>OUI</span><span class="box"></span>NON</div>
        <div class="col" style="width:48px"></div>
      </div>
      <div class="opt-row">
        <div class="lab"><strong>Echantillons supplémentaires</strong><br>24 bouteilles supplémentaires</div>
        <div class="col yn" style="padding-top:6px"><span class="box"></span><span>OUI</span><span class="box"></span>NON</div>
        <div class="col yn" style="padding-top:6px"><span class="box"></span><span>OUI</span><span class="box"></span>NON</div>
        <div class="col" style="width:48px"></div>
      </div>
      <div class="opt-total">TOTAL Options</div>
    </div>

    <p class="total-text"><strong>TOTAL FORMULE + OPTIONS RETENUES =</strong><br>
    Votre inscription ne sera validée qu'à réception d'un premier règlement de 50% du montant total indiqué ci-dessus. Le solde devant être réglé au plus tard 15 jours avant, dans le cas contraire, l'accès vous sera refusé. Paiement par transfert bancaire en Euro.</p>

    <div class="bank">
      <dl>
        <dt>Bank Name</dt><dd>: Harbour Trust Bank</dd>
        <dt>Swift Code</dt><dd>: HTBKHKHHXXX</dd>
        <dt>Bank address</dt><dd>: 8 Harbour Lane, Central, Hong Kong</dd>
        <dt>Account name</dt><dd>: VINELLE EVENTS LTD</dd>
        <dt>Account No</dt><dd>: 000-123456-789</dd>
      </dl>
      <p class="note">Merci d'identifier votre transfert par "EWDT – votre société", et merci de ne déduire aucune charge bancaire liée au transfert, qui reste à votre charge.</p>
    </div>
    <p class="footnote">Règlement sur les conditions générales de vente sur demande à : contact@vinelle-events.net</p>
  </div>
</section>

</body>
</html>
```